Design of an attractive membership brochure/membership card for an Electrical Business

Hi, we are an electrical business based in Sydney, Australia.

Our design's aim is to attract and target new customers into using our business as a repeat for anything electrical in their home. We would be handing this out to them after a job is completed and they're happy with the service.
We're thinking of a brochure, possibly additional membership cards with personalized number ID's for each client.

Open to ideas, but some of the things we want to include on our brochure are perks of why the client should sign up with us as a lifetime client
- Discounted emergency call out fees outside of normal hours
- Lifetime membership price, one time payment
- Exclusive 10% member discount on all future jobs
- Priority on any during business hour jobs or emergencies

If any other questions please don't hesitate to reach out.
We've attached our logo for reference for the mock designs.
Our website
https://brightwirecrew.com.au/

```html
<!DOCTYPE html>
<html lang="en">
<head>
<meta charset="utf-8">
<title>Bright Wire Crew – Membership Brochure</title>
<link href="https://fonts.googleapis.com/css2?family=Montserrat:wght@300;400;600;700&family=Playfair+Display:ital,wght@0,700;1,700&display=swap" rel="stylesheet">
<style>
:root{
  --red:#e8332a;
  --red-deep:#a50f1e;
  --wine:#5e0a14;
  --charcoal:#3c3d41;
  --ink:#17181b;
  --card:#d8d8da;
  --card-text:#3a3a3d;
  --white:#ffffff;
  --stage:#e9e9e7;
  --sans:'Montserrat',sans-serif;
  --serif:'Playfair Display',serif;
}
*{box-sizing:border-box;margin:0;padding:0}
html,body{width:1200px;height:2666px;overflow:hidden;background:var(--stage);font-family:var(--sans)}
.spread{position:absolute;left:60px;width:1080px;height:764px;display:flex;box-shadow:0 14px 34px rgba(0,0,0,.18)}
.spread--cover{top:60px}
.spread--about{top:904px}
.spread--services{top:1748px}
.page{position:relative;width:540px;height:764px;overflow:hidden}
.shape{position:absolute;inset:0}

/* brand name */
.brand{display:flex;align-items:center;gap:10px;font-family:var(--sans);font-weight:700;letter-spacing:3px;text-transform:uppercase;color:var(--red);white-space:nowrap}
.brand__mark{width:14px;height:14px;background:currentColor;flex:none}
.brand--light{color:var(--white)}

/* front cover */
.cover-front{background:var(--white)}
.cover-front .brand{position:absolute;left:50px;top:100px;font-size:23px;letter-spacing:2px;z-index:1}
.cover-front .brand__mark{width:12px;height:12px}
.cover-front__pitch{position:absolute;right:14px;bottom:70px;width:270px;color:var(--white);text-align:center;font-family:var(--sans);transform:rotate(-9deg);white-space:nowrap}
.pitch__lead{font-size:15px;font-weight:400}
.pitch__main{font-size:19px;font-weight:700;line-height:1.2}
.pitch__city{font-size:22px;font-weight:700;line-height:1.2}
.pitch__cta{font-size:9.5px;font-weight:400;margin-top:5px}
.pitch__cta strong{font-weight:700}

/* back cover */
.cover-back{background:linear-gradient(150deg,#c31a2c 0%,var(--red-deep) 45%,var(--wine) 100%)}
.cover-back__glow{position:absolute;right:-40px;top:200px;width:330px;height:380px;border-radius:50%;background:radial-gradient(circle,rgba(255,255,255,.12),rgba(255,255,255,0) 70%)}
.cover-back .brand{position:absolute;left:70px;top:300px;font-size:26px}
.contact{position:absolute;left:70px;top:370px;color:var(--white);font-family:var(--serif);font-weight:700}
.contact__label{font-size:12px;margin-bottom:6px}
.contact__email{font-size:12px;margin-bottom:6px}
.contact__phone{font-size:22px;margin-bottom:8px}
.contact__abn{font-size:16px;margin-bottom:14px}
.contact__licence{font-size:12px}
.contact__number{font-size:18px;margin-top:4px}

/* about page */
.about{background:var(--white)}
.about__photo-top{position:absolute;left:0;top:0;width:540px;height:340px;background:linear-gradient(160deg,#efe2c8 0%,#c79b63 35%,#7a5434 70%,#3b2a1f 100%)}
.about__band{position:absolute;left:0;top:270px;width:540px;height:330px;background:var(--red);clip-path:polygon(0 22%,100% 0,100% 78%,0 100%)}
.about__text{position:absolute;left:36px;top:345px;width:470px;color:var(--white)}
.about__title{font-family:var(--serif);font-style:italic;font-size:24px;margin-bottom:10px}
.about__text p{font-size:10px;line-height:1.55;margin-bottom:10px}
.collage{position:absolute;left:0;top:600px;width:540px;height:164px;display:grid;grid-template-columns:repeat(5,1fr);gap:3px;background:var(--white)}
.collage__tile{height:100%}
.tile--house{background:linear-gradient(#2a3a5a,#14192a)}
.tile--kitchen{background:linear-gradient(#f3f3f1,#c9cbcd)}
.tile--lounge{background:linear-gradient(#9aa0a6,#3f4449)}
.tile--garden{background:linear-gradient(#3b4a2c,#1b2216)}
.tile--interior{background:linear-gradient(#e6c99a,#8b6a45)}

/* services pages */
.services{background:var(--charcoal);padding:34px 28px 0}
.services__head{color:var(--white);margin-bottom:26px}
.services__title{font-family:var(--serif);font-weight:700;font-size:26px;line-height:1}
.services__rule{height:1px;background:var(--white);width:220px;margin:6px 0 4px}
.services__tag{font-size:8px;letter-spacing:.5px}
.cards{display:grid;grid-template-columns:repeat(3,1fr);gap:26px 12px}
.card{position:relative;background:var(--card);padding:24px 10px 12px;min-height:268px;color:var(--card-text)}
.card__icon{position:absolute;left:50%;top:-13px;margin-left:-14px;width:28px;height:28px;border-radius:50%;background:var(--red);display:flex;align-items:center;justify-content:center}
.card__icon svg{width:16px;height:16px}
.card__title{font-family:var(--serif);font-style:italic;font-weight:700;font-size:11px;line-height:1.2;margin-bottom:8px;text-align:center}
.card__text{font-size:8.3px;line-height:1.5;font-weight:400}
.services__foot{position:absolute;left:28px;right:28px;bottom:22px;display:flex;align-items:flex-end;justify-content:space-between}
.services__url{color:var(--white);font-family:var(--serif);font-size:11px;letter-spacing:2px}
.services__line{position:absolute;left:0;right:0;bottom:-8px;height:1px;background:var(--red)}
.services__foot .brand{font-size:13px;letter-spacing:2px}
.services__foot .brand__mark{width:8px;height:8px}

.services--extra .cards{grid-template-columns:1fr;width:240px;gap:26px}
.services--extra .card{min-height:150px}
.services__photo{position:absolute;right:0;top:0;width:260px;height:430px;background:linear-gradient(180deg,#f2f2f3 0%,#b8babd 40%,#2c2d30 75%,#e2e3e4 100%)}
.perks{position:absolute;left:0;right:0;top:450px;height:230px;background:linear-gradient(120deg,#3a0a10,#6e0f19 55%,#4a0a12);padding:40px 40px 0 70px}
.perks__list{color:var(--white);font-family:var(--serif);font-weight:700;font-size:14px;line-height:1.45}
.perks__list li{margin-bottom:6px}
</style>
</head>
<body>

<svg width="0" height="0" style="position:absolute" aria-hidden="true">
  <defs>
    <symbol id="i-bulb" viewBox="0 0 16 16"><path d="M8 2a4 4 0 0 0-2.5 7.1V11h5V9.1A4 4 0 0 0 8 2zM6 12.5h4M6.8 14h2.4" fill="none" stroke="#fff" stroke-width="1.3"/></symbol>
    <symbol id="i-bolt" viewBox="0 0 16 16"><path d="M9 1L3 9h4l-1 6 6-8H8z" fill="#fff"/></symbol>
    <symbol id="i-bell" viewBox="0 0 16 16"><path d="M4 11V7a4 4 0 0 1 8 0v4l1 1H3zM7 14h2" fill="none" stroke="#fff" stroke-width="1.3"/></symbol>
    <symbol id="i-tower" viewBox="0 0 16 16"><path d="M8 2v12M5 14l3-9 3 9M4 5h8" fill="none" stroke="#fff" stroke-width="1.3"/></symbol>
    <symbol id="i-fan" viewBox="0 0 16 16"><circle cx="8" cy="8" r="1.6" fill="#fff"/><path d="M8 6.4C7 3 10 2 10.5 4S9 6.5 8 6.4zM9.5 8.8c3 1 2.6 4 .6 3.8S8.7 9.6 9.5 8.8zM6.5 8.8c-3 .4-4-2.6-2.2-3.4S7 7.8 6.5 8.8z" fill="#fff"/></symbol>
    <symbol id="i-plug" viewBox="0 0 16 16"><rect x="3" y="3" width="10" height="10" rx="2" fill="none" stroke="#fff" stroke-width="1.3"/><path d="M6.5 6v2M9.5 6v2M8 10v1" stroke="#fff" stroke-width="1.3"/></symbol>
    <symbol id="i-search" viewBox="0 0 16 16"><circle cx="7" cy="7" r="4" fill="none" stroke="#fff" stroke-width="1.4"/><path d="M10 10l4 4" stroke="#fff" stroke-width="1.4"/></symbol>
    <symbol id="i-board" viewBox="0 0 16 16"><rect x="2" y="4" width="12" height="8" rx="1" fill="none" stroke="#fff" stroke-width="1.3"/><path d="M5 6v4M8 6v4M11 6v4" stroke="#fff" stroke-width="1.3"/></symbol>
    <symbol id="i-water" viewBox="0 0 16 16"><rect x="4" y="2" width="8" height="12" rx="2" fill="none" stroke="#fff" stroke-width="1.3"/><path d="M6 9h4" stroke="#fff" stroke-width="1.3"/></symbol>
    <symbol id="i-tv" viewBox="0 0 16 16"><rect x="2" y="4" width="12" height="8" rx="1" fill="none" stroke="#fff" stroke-width="1.3"/><path d="M6 14h4" stroke="#fff" stroke-width="1.3"/></symbol>
    <symbol id="i-wifi" viewBox="0 0 16 16"><path d="M2 6.5a9 9 0 0 1 12 0M4.3 9a5.5 5.5 0 0 1 7.4 0" fill="none" stroke="#fff" stroke-width="1.3"/><circle cx="8" cy="12" r="1.2" fill="#fff"/></symbol>
    <symbol id="i-home" viewBox="0 0 16 16"><path d="M2 8l6-5 6 5M4 7v6h8V7" fill="none" stroke="#fff" stroke-width="1.3"/></symbol>
    <symbol id="i-oven" viewBox="0 0 16 16"><rect x="3" y="2" width="10" height="12" rx="1" fill="none" stroke="#fff" stroke-width="1.3"/><path d="M3 6h10" stroke="#fff" stroke-width="1.3"/><circle cx="8" cy="10" r="2" fill="none" stroke="#fff" stroke-width="1.2"/></symbol>
  </defs>
</svg>

<!-- outer cover -->
<section class="spread spread--cover">
  <article class="page cover-back">
    <div class="cover-back__glow" role="img" aria-label="Faint photo of a hanging glass light bulb"></div>
    <div class="brand brand--light"><span class="brand__mark"></span>Bright Wire Crew</div>
    <div class="contact">
      <p class="contact__label">Contact Info</p>
      <p class="contact__email">services@brightwirecrew.com.au</p>
      <p class="contact__phone">0400 555 182</p>
      <p class="contact__abn">ABN - 12 345 678 901</p>
      <p class="contact__licence">Electrical Contractor Licence No.</p>
      <p class="contact__number">100200A</p>
    </div>
  </article>

  <article class="page cover-front">
    <svg class="shape" viewBox="0 0 540 764" width="540" height="764">
      <linearGradient id="g-bulbs-l" x1="0" y1="0" x2="1" y2="1">
        <stop offset="0" stop-color="#2a2d33"/><stop offset=".55" stop-color="#4a4640"/><stop offset="1" stop-color="#141519"/>
      </linearGradient>
      <radialGradient id="g-bulbs-r" cx=".45" cy=".48" r=".6">
        <stop offset="0" stop-color="#c9a56a"/><stop offset=".3" stop-color="#3b3a3c"/><stop offset="1" stop-color="#0d0e11"/>
      </radialGradient>
      <polygon points="0,300 350,215 260,600 0,640" fill="url(#g-bulbs-l)" role="img" aria-label="Photo of blurred hanging vintage bulbs"/>
      <polygon points="440,0 540,0 540,420 300,520" fill="url(#g-bulbs-r)" role="img" aria-label="Photo of a glowing filament light bulb"/>
      <polygon points="300,520 540,420 540,764 210,764" fill="var(--red)"/>
    </svg>
    <div class="brand"><span class="brand__mark"></span>Bright Wire Crew</div>
    <div class="cover-front__pitch">
      <p class="pitch__lead">Are You Looking For</p>
      <p class="pitch__main">Electricians based in</p>
      <p class="pitch__city">SYDNEY?</p>
      <p class="pitch__cta">Call now and get a <strong>FREE QUOTATION</strong> today!</p>
    </div>
  </article>
</section>

<!-- about + services -->
<section class="spread spread--about">
  <article class="page about">
    <div class="about__photo-top" role="img" aria-label="Photo of a warmly lit living room with armchair and lamps"></div>
    <div class="about__band"></div>
    <div class="about__text">
      <h2 class="about__title">About Us - Bright Wire Crew</h2>
      <p>Bright Wire Crew is a Sydney-based electrical business specialising in electrical maintenance work for residential, commercial, strata and real estate clients. It began with two mates with a strong desire to change the image of tradies and provide exceptional service. As a team of electricians based in the Inner West of Sydney, we understand the need of everyday people struggling to find good, reliable and trustworthy electricians.</p>
      <p>At Bright Wire Crew, we have high expectations of ourselves and strive to improve every day. We're always available around the clock to provide professional advice or give a helping hand when in need.</p>
    </div>
    <div class="collage">
      <div class="collage__tile tile--house" role="img" aria-label="Photo of a house lit at dusk"></div>
      <div class="collage__tile tile--kitchen" role="img" aria-label="Photo of a bright white kitchen"></div>
      <div class="collage__tile tile--lounge" role="img" aria-label="Photo of a modern lounge with pendant lights"></div>
      <div class="collage__tile tile--garden" role="img" aria-label="Photo of garden lighting at night"></div>
      <div class="collage__tile tile--interior" role="img" aria-label="Photo of a warmly lit interior"></div>
    </div>
  </article>

  <article class="page services">
    <header class="services__head">
      <h2 class="services__title">Our Services</h2>
      <div class="services__rule"></div>
      <p class="services__tag">Customer Satisfaction Is Our Highest Priority</p>
    </header>
    <div class="cards">
      <div class="card"><span class="card__icon"><svg><use href="#i-bulb"/></svg></span>
        <h3 class="card__title">Lighting Layout Design And Installations</h3>
        <p class="card__text">We offer a range of lighting layout designs, installations, and repairs. We can supply and install general indoor lighting such as downlights, custom chandeliers, oyster lights and batten lights. We can even supply and install outdoor and decorative lighting such as floodlights, garden lighting, LED strip lights, bollards and security lights. We can even provide energy-saving solutions which can include sensors or timer lights.</p></div>
      <div class="card"><span class="card__icon"><svg><use href="#i-bolt"/></svg></span>
        <h3 class="card__title">Emergency Services</h3>
        <p class="card__text">We understand that having an electrical emergency is immensely stressful. That's why at Bright Wire Crew, we're available 24 hours to respond to any time-sensitive emergency work. Our vehicles come fully stocked with all the equipment to complete jobs at all hours. If you need an emergency electrician, don't hesitate to ring one of our team, and we'll be there.</p></div>
      <div class="card"><span class="card__icon"><svg><use href="#i-bell"/></svg></span>
        <h3 class="card__title">Smoke Alarm Installations And Testing</h3>
        <p class="card__text">Our team will install and test your smoke alarms. This is vital for the safety of your home or rental property. Bright Wire Crew will ensure your smoke alarms' visual and audio indicators are working as they should so that you know your family is safe.</p></div>
      <div class="card"><span class="card__icon"><svg><use href="#i-tower"/></svg></span>
        <h3 class="card__title">Level 2 Electrician</h3>
        <p class="card__text">Our team can provide a Level 2 Electrician to perform a wide variety of electrical connection services for our customers in Sydney. So give us a call if you need level 2 works regarding electrical defect notices, consumer mains, private power pole replacements, underground power, point of attachment, overhead &amp; underground power, 3-phase switchboard upgrades and/or general safety inspections.</p></div>
      <div class="card"><span class="card__icon"><svg><use href="#i-fan"/></svg></span>
        <h3 class="card__title">Ceiling Fans, Exhaust Fans &amp; General Ventilation</h3>
        <p class="card__text">Prepare for that summer heat with ceiling fans and make sure your rooms are mold-free! We'll supply, install, and warranty any ceiling fan we supply and install. No one wants mold on their walls and ceilings. Our technicians will make sure you have the appropriate exhaust fan that accounts for the size of your bathroom, laundry, or any room that can get damp.</p></div>
      <div class="card"><span class="card__icon"><svg><use href="#i-plug"/></svg></span>
        <h3 class="card__title">Powerpoint Installations Or Repair</h3>
        <p class="card__text">Sick of running messy power leads like it's Christmas decorations? Moving into a new home and there are not enough power points? We've got you covered. No installation is too big, no job is too small. We can wire new power points anywhere in your home. If you have any damaged or cracked power points, we also offer hassle-free replacements.</p></div>
    </div>
    <footer class="services__foot">
      <span class="services__url">www.brightwirecrew.com.au</span>
      <div class="brand"><span class="brand__mark"></span>Bright Wire Crew</div>
      <span class="services__line"></span>
    </footer>
  </article>
</section>

<!-- more services + membership perks -->
<section class="spread spread--services">
  <article class="page services">
    <header class="services__head">
      <h2 class="services__title">Our Services</h2>
      <div class="services__rule"></div>
      <p class="services__tag">Customer Satisfaction Is Our Highest Priority</p>
    </header>
    <div class="cards">
      <div class="card"><span class="card__icon"><svg><use href="#i-search"/></svg></span>
        <h3 class="card__title">Electrical Fault Finding</h3>
        <p class="card__text">It is quite common for electrical faults to happen in your home. This can cause a loss of power, or worst case, damage to your property. Bright Wire Crew are experts in the trade, equipped with the know-how to locate each problem head-on. We'll diagnose and provide a solution for your electrical issues, whether it be a loss of power, lights, or even flickering lights.</p></div>
      <div class="card"><span class="card__icon"><svg><use href="#i-bolt"/></svg></span>
        <h3 class="card__title">Surge Protection</h3>
        <p class="card__text">Do you have a TV or an expensive appliance in your home? Think of getting a surge protection device. Surges are spikes in power from storms, lightning, or electrical grid fluctuations. Surges can cause appliances to turn off or malfunction. Having a device like a surge protector in your home will save you all the headaches!</p></div>
      <div class="card"><span class="card__icon"><svg><use href="#i-board"/></svg></span>
        <h3 class="card__title">Switchboard Upgrade And Repairs</h3>
        <p class="card__text">Switchboards are the heart of your home. We'll ensure your switchboard or sub-boards has all the necessary overload protection and safety devices in place. At Bright Wire Crew, our electricians are fully trained and qualified to work with your switchboard. We can repair, relocate, replace, or even install a brand-new switchboard for you with all the latest protection devices.</p></div>
      <div class="card"><span class="card__icon"><svg><use href="#i-water"/></svg></span>
        <h3 class="card__title">Hot Water Diagnosis &amp; Repair</h3>
        <p class="card__text">Here at Bright Wire Crew, we do 24/7 hot water repairs. Whether it's a problem with the fuse, circuit breaker, or wiring connections. Our vans are always stocked, so we'll efficiently diagnose and repair your issue to ensure your hot water returns as soon as possible.</p></div>
      <div class="card"><span class="card__icon"><svg><use href="#i-tv"/></svg></span>
        <h3 class="card__title">TV Antenna Installation &amp; Diagnostics</h3>
        <p class="card__text">Our team is fully equipped to install your TV aerial, TV connection point, and wall mount your TV. We'll ensure your cabling is organized and neatly concealed but easily accessible.</p></div>
      <div class="card"><span class="card__icon"><svg><use href="#i-wifi"/></svg></span>
        <h3 class="card__title">Data &amp; Nbn</h3>
        <p class="card__text">Our team can install multiple data locations or WiFi access points throughout your home to make sure your speed is always performing at its best.</p></div>
    </div>
    <footer class="services__foot">
      <span class="services__url">www.brightwirecrew.com.au</span>
      <div class="brand"><span class="brand__mark"></span>Bright Wire Crew</div>
      <span class="services__line"></span>
    </footer>
  </article>

  <article class="page services services--extra">
    <div class="services__photo" role="img" aria-label="Photo of a modern white bathroom with a crystal chandelier"></div>
    <header class="services__head">
      <h2 class="services__title">Our Services</h2>
      <div class="services__rule"></div>
      <p class="services__tag">Customer Satisfaction Is Our Highest Priority</p>
    </header>
    <div class="cards">
      <div class="card"><span class="card__icon"><svg><use href="#i-home"/></svg></span>
        <h3 class="card__title">Renovation And Fitouts</h3>
        <p class="card__text">Whether you're renovating your kitchen, bathroom, or your entire house, we can install all your power, lighting, and data cabling requirements to ensure you're enjoying all the benefits of modern living.</p></div>
      <div class="card"><span class="card__icon"><svg><use href="#i-oven"/></svg></span>
        <h3 class="card__title">Appliance Installation</h3>
        <p class="card__text">Our team will install your new oven, cooktop, or rangehood. We take pride in our workmanship and handle all appliances with care as if they were our own.</p></div>
    </div>
    <div class="perks">
      <ul class="perks__list">
        <li>Discounted emergency call out fees outside of normal hours</li>
        <li>Lifetime membership price, one time payment</li>
        <li>Exclusive 10% member discount on all future jobs</li>
        <li>Priority on any during business hour jobs or emergencies</li>
      </ul>
    </div>
    <footer class="services__foot">
      <span class="services__url">www.brightwirecrew.com.au</span>
      <div class="brand"><span class="brand__mark"></span>Bright Wire Crew</div>
      <span class="services__line"></span>
    </footer>
  </article>
</section>

</body>
</html>
```